Brindel's Coating & Renewal Letterhead Design We want to revamp out old traditional letterhead with the new logo designs that are attached. We are working on getting all our company items from vehicles, business, cards, t-shirts, letterhead to match. This should include company colors, fonts, and flow of items that we have attached below.

Industry/Entity Type

Construction Company

Font styles to use
Sans Serif
Other font styles liked:
• Bold with outline

Colors
ec1f27
ffffff

Requirements
Must have
• Company Name: Brindel's Coating & Renewal
• Address: 4217 SW 83rd Ter Marlow Cove fl 33418
• Office Number: (954) 555-0194
• Email: Brindelrenewal@quorvane.com
• License Number: CGC8064392
Nice to have
• Company Colors: red, white, black, and grey

```html
<!DOCTYPE html>
<html lang="en">
<head>
<meta charset="utf-8">
<title>Brindel's Coating &amp; Renewal – Letterhead</title>
<link rel="stylesheet" href="https://fonts.googleapis.com/css2?family=Montserrat:wght@400;500;600;700&display=swap">
<style>
  :root {
    --brand-red: #ec1f27;
    --accent-orange: #ef4a26;
    --ink: #333333;
    --wash-grey: #ececec;
    --wash-blush: #fcdfd8;
    --paper: #ffffff;
  }
  * { margin: 0; padding: 0; box-sizing: border-box; }
  html, body {
    width: 889px; height: 1200px; overflow: hidden;
    background: var(--paper);
  }
  body { font-family: "Montserrat", sans-serif; color: var(--ink); }
  .letterhead { position: relative; width: 889px; height: 1200px; background: var(--paper); overflow: hidden; }

  .wash { position: absolute; pointer-events: none; }
  .wash-top {
    right: 0; top: 0; width: 560px; height: 300px;
    background: radial-gradient(ellipse at 100% 0%, var(--wash-grey) 0%, rgba(236,236,236,0.5) 40%, rgba(255,255,255,0) 72%);
  }
  .wash-bottom {
    right: 0; bottom: 0; width: 700px; height: 90px;
    background: linear-gradient(90deg, rgba(255,255,255,0) 0%, rgba(252,223,216,0.55) 55%, var(--wash-blush) 100%);
  }

  .brand-name {
    position: absolute; left: 62px; top: 40px;
    color: var(--accent-orange); font-weight: 700; text-transform: uppercase;
    line-height: 1;
  }
  .brand-name .primary { display: block; font-size: 44px; letter-spacing: 1px; }
  .brand-name .secondary { display: block; font-size: 22px; margin-top: 12px; letter-spacing: 1.5px; }

  .contact { position: absolute; right: 67px; top: 72px; list-style: none; }
  .contact li {
    display: flex; align-items: center; justify-content: flex-end;
    font-size: 16px; font-weight: 600; height: 21px;
  }
  .contact svg { width: 18px; height: 18px; margin-left: 9px; flex: none; }

  .rule { position: absolute; height: 2px; background: var(--brand-red); }
  .rule-top { left: 62px; width: 758px; top: 165px; }
  .rule-bottom { left: 0; width: 889px; top: 1119px; }

  .closing { position: absolute; left: 62px; top: 238px; font-size: 13.5px; }
  .signatory { position: absolute; left: 62px; top: 274px; }
  .signatory .name { font-size: 23px; font-weight: 700; letter-spacing: 0.5px; line-height: 1; }
  .signatory .role { font-size: 16px; font-weight: 600; margin-top: 6px; line-height: 1; }

  .body-copy {
    position: absolute; left: 62px; font-size: 13.4px; line-height: 28px;
    white-space: nowrap; letter-spacing: 0.1px;
  }
  .para-1 { top: 458px; }
  .para-2 { top: 654px; }
  .para-3 { top: 794px; }

  .footer-address { position: absolute; left: 62px; top: 1135px; font-size: 17px; font-weight: 700; }
  .footer-license { position: absolute; right: 68px; top: 1135px; font-size: 17px; font-weight: 700; color: var(--brand-red); }
</style>
</head>
<body>
<main class="letterhead">
  <div class="wash wash-top" role="img" aria-label="Soft grey decorative accent"></div>
  <div class="wash wash-bottom" role="img" aria-label="Soft blush decorative accent"></div>

  <h1 class="brand-name">
    <span class="primary">Brindel's</span>
    <span class="secondary">Coating &amp; Renewal</span>
  </h1>

  <ul class="contact">
    <li>(954) 555-0194
      <svg viewBox="0 0 20 20"><circle cx="10" cy="10" r="9" fill="none" stroke="var(--accent-orange)" stroke-width="1.4"/><path d="M7 5.5l1.6 2.4-1 1c.6 1.4 1.6 2.4 3 3l1-1 2.4 1.6-.9 1.6C9.5 14.2 5.8 10.5 5.7 6.4z" fill="var(--accent-orange)"/></svg>
    </li>
    <li>Brindelrenewal@quorvane.com
      <svg viewBox="0 0 20 20"><circle cx="10" cy="10" r="9" fill="none" stroke="var(--accent-orange)" stroke-width="1.4"/><rect x="5.5" y="7" width="9" height="6" fill="var(--accent-orange)"/><path d="M5.5 7l4.5 3.5L14.5 7" fill="none" stroke="#fff" stroke-width="0.9"/></svg>
    </li>
    <li>www.brindelrenewal
      <svg viewBox="0 0 20 20"><circle cx="10" cy="10" r="9" fill="none" stroke="var(--accent-orange)" stroke-width="1.4"/><g fill="none" stroke="var(--accent-orange)" stroke-width="0.9"><circle cx="10" cy="10" r="4.8"/><ellipse cx="10" cy="10" rx="2" ry="4.8"/><path d="M5.2 10h9.6M5.9 7.6h8.2M5.9 12.4h8.2"/></g></svg>
    </li>
  </ul>

  <div class="rule rule-top"></div>

  <p class="closing">Sincearly,</p>
  <div class="signatory">
    <p class="name">DORIAN VALE</p>
    <p class="role">Director</p>
  </div>

  <p class="body-copy para-1">
    This is a sample letter that has been placed to demonstrate typing remat (Your Company).letterhead<br>
    design. When positioned properly, it will serve to work in harmony with all other elements letterhead.<br>
    This letterhead design is meant to project an image&nbsp; This letterhead design is meant project an image<br>
    of professionalism reliability. By using simple aligen we have created a very spacious feeling.<br>
    The simplicity suggest&nbsp; rengththe spaciousnes contributes haesthetics the layout. These basic<br>
    qualities along with the (Your Company)
  </p>
  <p class="body-copy para-2">
    look and helps reinforce the (Your Company) brand. letterhead design is meant to project an image<br>
    design. When positioned properly, it will serve to work in harmony all the other elements letterhead.<br>
    sionalism and reliability.
  </p>
  <p class="body-copy para-3">
    This letterhead design is based on the (Form of your logo) form (Your Company) logo. Each stationery<br>
    we have created a very spacious feeling. The simplicity suggests strength the spaciousnes contribute<br>
    part of the (Form of your logo). This letterhead design is based on the (Form of your logo) form (Your<br>
    Company) logo. Each stationery we have created a very spacious feeling. The simplicity suggests<br>
    strength the spaciousnes contribute part of the (Form of your logo).
  </p>

  <div class="rule rule-bottom"></div>
  <p class="footer-address">4217 SW 83rd Ter . Marlow Cove, Florida 33418</p>
  <p class="footer-license">CGC8064392</p>
</main>
</body>
</html>
```